Trying to create a web site off this static page

I am trying to create a seperate web site for this specific page. https://brellowathletics.com/hire-a-star/ I am still trying to figure out the domain name, for now, I will use Gold Roster as the name. I want to use the same pictures, but much more eye catching. Help me come up with something nice, something i can use to market to my thousands of customers. Maybe some flash. Something dramatic. I have some more content that I would like to add as well, but in the meantime, lets see what you come up with. Good luck and thanks
Updates

Some of these are really great. I may extend this for a few days... Please is the pictures from the Brellow Athletics web site, but I want to make a few changes.... I want the name of the site changes to LumaHours.com and as far as columns and tabs on the site, These are the tabs that I want. Please work with these and make the changes.

Our Talent

Past Client Experiences

ABout Us ( Our Philosophy)

Our Process

Ideas

Business Opportunities/ Warm Introductions

For the front page, I would like this content added in

FRONT PAGE Use this tag line somewhere "Where Dreams Become VIP Experiences
Exclusive talent. Tailored events. Memories that last a lifetime."

Welcome to Luma Hours

Where unforgettable moments are made.

At Luma Hours, we connect individuals, businesses, and organizations with the world’s most recognizable athletes, entertainers, and celebrities. Whether it’s a private celebration, a corporate event, or a once-in-a-lifetime experience, our team specializes in making the impossible possible.

What We Do

Celebrity Bookings – From iconic musicians to legendary athletes, we secure top-tier talent for parties, concerts, and corporate functions.

Corporate Engagements – Motivate, inspire, and entertain your team with appearances from world-class speakers and sports legends.

Private Experiences – Fishing trips with Crest Final champions, golf outings with All-Stars, tequila tastings with Hall of Famers—our clients have done it all.

University & Charity Events – Elevate your fundraiser, gala, or campus program with star power that draws attention and delivers impact.

VIP Appearances – From sitting courtside at the Summit Classic with an PLH legend to sparring with Dale Crowder, no dream is too big.

Why Choose Luma Hours?

Exclusive Access – We work directly with celebrities and their management teams to deliver authentic, unforgettable experiences.

Proven Track Record – From Meridian 400 companies to private clients, we’ve orchestrated events with some of the most famous names in the world.

Custom Experiences – Every event is unique. We tailor each booking to fit your vision, budget, and audience.

Confidential & Professional – Our clients trust us to deliver world-class experiences with complete discretion and flawless execution.

Let’s Make It Happen

Whether you’re planning a corporate retreat, a milestone celebration, or a private experience you’ll never forget, LumaHours.com is your partner in making it extraordinary.

👉 If you can dream it, we can make it happen.

```html
<!DOCTYPE html>
<html lang="en">
<head>
<meta charset="utf-8">
<title>Gold Roster – Where Dreams Become VIP Experiences</title>
<link href="https://fonts.googleapis.com/css2?family=Bebas+Neue&family=Poppins:wght@400;500;600;700&display=swap" rel="stylesheet">
<style>
:root{
  --navy:#10124f;
  --navy-deep:#0b0c35;
  --footer:#0a0b2b;
  --red:#e11b1f;
  --red-dark:#b3121a;
  --white:#ffffff;
  --ink:#161616;
  --muted:#4a4a4a;
  --soft:#ececec;
  --field:#f1f1f1;
}
*{margin:0;padding:0;box-sizing:border-box}
html,body{width:1200px;height:5029px;overflow:hidden}
body{position:relative;font-family:'Poppins',sans-serif;color:var(--ink);background:var(--white)}
.abs{position:absolute}
.display{font-family:'Bebas Neue',sans-serif;font-weight:400;letter-spacing:.5px;line-height:1}

/* buttons */
.btn-wrap{position:absolute;display:flex;align-items:center}
.btn{flex:none;display:flex;align-items:center;justify-content:center;gap:10px;height:100%;width:calc(100% - 26px);padding:0 20px 0 14px;background:var(--red);color:var(--white);font:700 12.5px/1 'Poppins',sans-serif;letter-spacing:.4px;text-transform:uppercase;white-space:nowrap;clip-path:polygon(0 0,calc(100% - 16px) 0,100% 100%,0 100%)}
.btn svg{width:9px;height:12px;flex:none}
.btn-wrap::before,.btn-wrap::after{content:"";position:absolute;top:0;bottom:0;width:5px;background:var(--red);transform:skewX(32deg);transform-origin:top}
.btn-wrap::before{right:14px}
.btn-wrap::after{right:4px}

/* top bar + nav */
.topbar{left:687px;top:0;width:513px;height:35px;background:var(--red);clip-path:polygon(12px 0,100% 0,100% 100%,0 100%);display:flex;align-items:center;gap:60px;padding-left:38px;color:var(--white);font-size:13px;font-weight:500;white-space:nowrap}
.topbar span{display:flex;align-items:center;gap:14px}
.topbar svg{width:14px;height:14px}
.logo{color:var(--white);font-family:'Bebas Neue',sans-serif;font-size:30px;letter-spacing:.5px;white-space:nowrap}
.nav{left:259px;top:70px;display:flex;gap:22px;color:var(--white);font-size:13px;white-space:nowrap}

/* hero */
.hero{left:0;top:0;width:1200px;height:712px;background:var(--navy);overflow:hidden}
.hero-photo{left:0;top:0;width:1200px;height:712px;background:radial-gradient(ellipse at 62% 38%,#5a2742 0%,#3a1f4f 30%,#1b1a5c 60%,var(--navy) 100%)}
.hero-shade{left:0;top:0;width:1200px;height:712px;background:linear-gradient(90deg,rgba(16,18,79,.9) 0%,rgba(16,18,79,.35) 55%,rgba(16,18,79,.2) 100%)}
.hero h1{left:107px;top:218px;color:var(--white);font-size:58px;line-height:1.02}
.hero .lede{left:107px;top:350px;color:var(--white);font-family:'Bebas Neue',sans-serif;font-size:27px;letter-spacing:.2px;white-space:nowrap}
.slider-dots{left:50px;top:305px;display:flex;flex-direction:column;gap:13px}
.slider-dots i{display:block;width:10px;height:10px;border-radius:50%;background:#5d5f8a}
.slider-dots i:first-child{background:var(--red)}
.social-rail{left:1114px;top:302px;display:flex;flex-direction:column;gap:15px}
.social-rail i{display:block;width:13px;height:13px;border-radius:50%;background:var(--white)}

/* welcome */
.welcome{left:0;top:712px;width:1200px;height:529px;background:var(--navy);overflow:hidden}
.ghost{font-family:'Bebas Neue',sans-serif;white-space:nowrap;line-height:.8}
.welcome h2{left:611px;top:66px;color:var(--white);font-size:48px;white-space:nowrap}
.welcome .sub{left:611px;top:120px;color:var(--white);font-family:'Bebas Neue',sans-serif;font-size:22px;letter-spacing:.3px;white-space:nowrap}
.welcome p{left:611px;top:160px;width:430px;color:#6c6e96;font-size:14.5px;line-height:1.65}

/* what we do */
.what{left:0;top:1241px;width:1200px;height:1998px;background:var(--white);overflow:hidden}
.section-title{color:var(--navy-deep);font-size:44px;text-align:center;width:1200px;left:0}
.card-title{font-weight:600;font-size:20px;color:var(--ink);white-space:nowrap}
.card-text{font-size:14.5px;line-height:1.62;color:var(--ink);width:360px}

/* why us */
.why{left:0;top:3239px;width:1200px;height:741px;background:var(--soft);border-top:14px solid var(--red);overflow:hidden}
.why-title{color:var(--red);font-weight:600;font-size:18.5px;white-space:nowrap}
.why-text{font-size:14.5px;line-height:1.62;color:#333;width:260px}
.right-align{text-align:right}

/* quote */
.quote{left:0;top:3980px;width:1200px;height:640px;background:var(--navy);overflow:hidden}
.quote h2{left:107px;top:186px;color:var(--white);font-size:46px;white-space:nowrap}
.quote p{left:107px;top:236px;width:440px;color:var(--white);font-size:14.5px;line-height:1.62}
.form-card{left:726px;top:78px;width:359px;height:429px;background:var(--white)}
.form-card h3{position:absolute;left:0;top:52px;width:100%;text-align:center;color:var(--navy-deep);font-size:34px}
.field{position:absolute;height:34px;background:var(--field);border:1px solid #e2e2e2;font-size:11px;color:#333;padding:8px 10px}

/* footer */
.footer{left:0;top:4481px;width:1200px;height:548px;background:var(--footer)}
.foot-links{left:107px;top:230px;display:flex;gap:22px;color:#c9c9d8;font-size:12.5px;white-space:nowrap}
.foot-contact{left:933px;top:196px;color:var(--white);font-size:13px;font-weight:600;display:flex;flex-direction:column;gap:10px;white-space:nowrap}
.foot-contact span{display:flex;align-items:center;gap:10px}
.foot-contact svg{width:13px;height:13px}
.divider{left:107px;top:293px;width:986px;height:1px;background:#23254a}
.foot-social{left:517px;top:354px;display:flex;gap:12px}
.foot-social i{display:block;width:24px;height:24px;border:2px solid var(--white);border-radius:50%}
.copy{left:0;top:400px;width:1200px;text-align:center;color:#c9c9d8;font-size:12.5px}
.copy b{color:var(--red);font-weight:400}
</style>
</head>
<body>

<!-- HERO -->
<header class="hero abs">
  <div class="hero-photo abs" role="img" aria-label="Concert stage with lighting rig and a celebrity posing with fans in the crowd"></div>
  <div class="hero-shade abs"></div>
  <h1 class="display abs">Where Dreams Become<br>VIP Experiences</h1>
  <div class="lede abs">Exclusive talent. Tailored events. Memories that last a lifetime.</div>
  <div class="btn-wrap" style="left:107px;top:410px;width:190px;height:45px"><span class="btn">Get in touch <svg viewBox="0 0 9 12"><path d="M2 1l5 5-5 5" stroke="#fff" stroke-width="2" fill="none"/></svg></span></div>
  <div class="slider-dots abs"><i></i><i></i><i></i><i></i><i></i><i></i><i></i></div>
  <div class="social-rail abs"><i></i><i></i><i></i><i></i><i></i></div>
  <svg class="abs" style="left:0;top:560px" width="1200" height="152" viewBox="0 0 1200 152">
    <polygon points="0,152 0,128 599,20 1200,128 1200,152 1200,160 599,60 0,160" fill="var(--red)"/>
    <polygon points="0,152 599,52 1200,152" fill="var(--navy)"/>
    <circle cx="599" cy="31" r="28" fill="var(--red)" stroke="#fff" stroke-width="3"/>
    <path d="M599 18v24M589 33l10 10 10-10" stroke="#fff" stroke-width="4" fill="none" stroke-linecap="round"/>
  </svg>
</header>

<div class="topbar abs">
  <span><svg viewBox="0 0 14 14"><rect x="1" y="3" width="12" height="8" rx="1" fill="#fff"/><path d="M1 3l6 5 6-5" stroke="var(--red)" fill="none"/></svg>hello@goldroster.com</span>
  <span><svg viewBox="0 0 14 14"><path d="M3 1l3 3-1.5 2a8 8 0 0 0 3.5 3.5L10 8l3 3-2 2C6 13 1 8 1 3z" fill="#fff"/></svg>(555) 018-2947</span>
</div>
<div class="logo abs" style="left:107px;top:60px">Gold Roster</div>
<nav class="nav abs"><span>Our Talent</span><span>Past Client Experiences</span><span>About Us</span><span>Our Process</span><span>Ideas</span><span>Business Opportunities</span></nav>
<div class="btn-wrap" style="left:919px;top:55px;width:176px;height:50px"><span class="btn" style="font-size:13.5px">Book now <svg viewBox="0 0 9 12"><path d="M2 1l5 5-5 5" stroke="#fff" stroke-width="2" fill="none"/></svg></span></div>

<!-- WELCOME -->
<section class="welcome abs">
  <div class="ghost abs" style="left:190px;top:-60px;font-size:230px;color:#141763">WELCOME</div>
  <div class="ghost abs" style="left:95px;top:330px;font-size:210px;color:#141763">GOLD ROSTER</div>
  <svg class="abs" style="left:107px;top:35px" width="453" height="410" viewBox="0 0 453 410" role="img" aria-label="Photo collage of the team with sports legends at a signing event">
    <defs>
      <linearGradient id="wg1" x1="0" y1="0" x2="1" y2="1"><stop offset="0" stop-color="#2b2b33"/><stop offset="1" stop-color="#6a5a55"/></linearGradient>
      <linearGradient id="wg2" x1="0" y1="0" x2="1" y2="1"><stop offset="0" stop-color="#3a3a44"/><stop offset="1" stop-color="#8a7a70"/></linearGradient>
    </defs>
    <polygon points="0,0 390,0 320,300 0,300" fill="url(#wg1)"/>
    <polygon points="325,300 345,220 375,220 355,300" fill="var(--red)"/>
    <polygon points="30,300 330,300 322,330 22,330" fill="var(--red)"/>
    <polygon points="300,252 453,252 453,410 245,410" fill="url(#wg2)"/>
  </svg>
  <h2 class="display abs">Welcome to Luma Hours</h2>
  <div class="sub abs">Where unforgettable moments are made.</div>
  <p class="abs">At Luma Hours, we connect individuals, businesses, and organizations with the world’s most recognizable athletes, entertainers, and celebrities. Whether it’s a private celebration, a corporate event, or a once-in-a-lifetime experience, our team specializes in making the impossible possible.</p>
  <div class="btn-wrap" style="left:611px;top:326px;width:190px;height:47px"><span class="btn">Get in touch <svg viewBox="0 0 9 12"><path d="M2 1l5 5-5 5" stroke="#fff" stroke-width="2" fill="none"/></svg></span></div>
</section>

<!-- WHAT WE DO -->
<section class="what abs">
  <div class="ghost abs" style="left:95px;top:-60px;font-size:210px;color:#f3f3f3">GOLD ROSTER</div>
  <div class="ghost abs" style="font-size:200px;color:#e9e9e9;transform:rotate(-90deg);transform-origin:0 0;top:1640px;left:1110px">WHAT WE DO</div>
  <h2 class="section-title display abs" style="top:52px">What We Do</h2>

  <svg class="abs" style="left:107px;top:150px" width="473" height="351" viewBox="0 0 473 351" role="img" aria-label="Celebrity signing boxing gloves at a booking event">
    <defs><linearGradient id="c1" x1="0" y1="0" x2="1" y2="1"><stop offset="0" stop-color="#2a2a30"/><stop offset="1" stop-color="#7a6b66"/></linearGradient></defs>
    <polygon points="0,0 330,0 473,351 0,351" fill="url(#c1)"/>
    <polygon points="330,0 350,0 473,300 473,351" fill="var(--red)"/>
  </svg>
  <div class="card-title abs" style="left:107px;top:529px">Celebrity Bookings</div>
  <div class="card-text abs" style="left:107px;top:563px">From iconic musicians to legendary athletes, we secure top-tier talent for parties, concerts, and corporate functions.</div>
  <div class="btn-wrap" style="left:107px;top:652px;width:190px;height:48px"><span class="btn">Get in touch <svg viewBox="0 0 9 12"><path d="M2 1l5 5-5 5" stroke="#fff" stroke-width="2" fill="none"/></svg></span></div>

  <svg class="abs" style="left:615px;top:150px" width="473" height="351" viewBox="0 0 473 351" role="img" aria-label="Speaker on stage addressing a full conference ballroom">
    <defs><linearGradient id="c2" x1="0" y1="0" x2="1" y2="1"><stop offset="0" stop-color="#3b2e2a"/><stop offset="1" stop-color="#8c7c70"/></linearGradient></defs>
    <polygon points="0,0 330,0 473,351 0,351" fill="url(#c2)"/>
    <polygon points="330,0 350,0 473,300 473,351" fill="var(--red)"/>
  </svg>
  <div class="card-title abs" style="left:613px;top:529px">Corporate Engagements</div>
  <div class="card-text abs" style="left:613px;top:563px">Motivate, inspire, and entertain your team with appearances from world-class speakers and sports legends.</div>
  <div class="btn-wrap" style="left:613px;top:652px;width:190px;height:48px"><span class="btn">Get in touch <svg viewBox="0 0 9 12"><path d="M2 1l5 5-5 5" stroke="#fff" stroke-width="2" fill="none"/></svg></span></div>

  <svg class="abs" style="left:107px;top:763px" width="473" height="351" viewBox="0 0 473 351" role="img" aria-label="Sports legend posing with a young fan and her father">
    <defs><linearGradient id="c3" x1="0" y1="0" x2="1" y2="1"><stop offset="0" stop-color="#6b5550"/><stop offset="1" stop-color="#c7a8a0"/></linearGradient></defs>
    <polygon points="0,0 330,0 473,351 0,351" fill="url(#c3)"/>
    <polygon points="330,0 350,0 473,300 473,351" fill="var(--red)"/>
  </svg>
  <div class="card-title abs" style="left:105px;top:1141px">Private Experiences</div>
  <div class="card-text abs" style="left:105px;top:1175px;width:450px">Fishing trips with Crest Final champions, golf outings with All-Stars, tequila tastings with Hall of Famers—our clients have done it all.</div>
  <div class="btn-wrap" style="left:107px;top:1266px;width:190px;height:48px"><span class="btn">Get in touch <svg viewBox="0 0 9 12"><path d="M2 1l5 5-5 5" stroke="#fff" stroke-width="2" fill="none"/></svg></span></div>

  <svg class="abs" style="left:615px;top:763px" width="473" height="351" viewBox="0 0 473 351" role="img" aria-label="Celebrities laughing and embracing at a charity gala">
    <defs><linearGradient id="c4" x1="0" y1="0" x2="1" y2="1"><stop offset="0" stop-color="#3a3f5c"/><stop offset="1" stop-color="#8a8fa8"/></linearGradient></defs>
    <polygon points="0,0 330,0 473,351 0,351" fill="url(#c4)"/>
    <polygon points="330,0 350,0 473,300 473,351" fill="var(--red)"/>
  </svg>
  <div class="card-title abs" style="left:611px;top:1147px">University &amp; Charity Events</div>
  <div class="card-text abs" style="left:611px;top:1181px">Elevate your fundraiser, gala, or campus program with star power that draws attention and delivers impact.</div>
  <div class="btn-wrap" style="left:611px;top:1276px;width:190px;height:48px"><span class="btn">Get in touch <svg viewBox="0 0 9 12"><path d="M2 1l5 5-5 5" stroke="#fff" stroke-width="2" fill="none"/></svg></span></div>

  <svg class="abs" style="left:365px;top:1371px" width="470" height="352" viewBox="0 0 470 352" role="img" aria-label="Large crowd of fans gathered with a champion holding a title belt">
    <defs><linearGradient id="c5" x1="0" y1="0" x2="1" y2="1"><stop offset="0" stop-color="#4a4c58"/><stop offset="1" stop-color="#9c8a84"/></linearGradient></defs>
    <polygon points="0,0 330,0 470,352 0,352" fill="url(#c5)"/>
    <polygon points="330,0 350,0 470,300 470,352" fill="var(--red)"/>
  </svg>
  <div class="card-title abs" style="left:363px;top:1756px">VIP Appearances</div>
  <div class="card-text abs" style="left:363px;top:1790px;width:440px">From sitting courtside at the Summit Classic with an PLH legend to sparring with Dale Crowder, no dream is too big.</div>
  <div class="btn-wrap" style="left:363px;top:1853px;width:190px;height:48px"><span class="btn">Get in touch <svg viewBox="0 0 9 12"><path d="M2 1l5 5-5 5" stroke="#fff" stroke-width="2" fill="none"/></svg></span></div>
</section>

<!-- WHY US -->
<section class="why abs">
  <div class="ghost abs" style="left:245px;top:14px;font-size:200px;color:#dedede">WHY US</div>
  <h2 class="section-title display abs" style="top:80px">Why Choose Luma Hours?</h2>
  <svg class="abs" style="left:384px;top:191px" width="430" height="430" viewBox="0 0 430 430">
    <circle cx="215" cy="215" r="203" fill="none" stroke="#222" stroke-width="2" stroke-dasharray="5 5"/>
    <circle cx="215" cy="215" r="180" fill="none" stroke="#2b2b2b" stroke-width="14"/>
  </svg>
  <div class="display abs" style="left:0;width:1200px;top:395px;text-align:center;font-size:48px;color:#1c1c1c">Gold Roster</div>

  <svg class="abs" style="left:408px;top:220px" width="90" height="90" viewBox="0 0 90 90"><circle cx="45" cy="45" r="42" fill="var(--red)" stroke="#fff" stroke-width="4"/><circle cx="45" cy="34" r="9" fill="none" stroke="#fff" stroke-width="3"/><path d="M29 62c2-10 8-15 16-15s14 5 16 15" fill="none" stroke="#fff" stroke-width="3"/></svg>
  <svg class="abs" style="left:700px;top:220px" width="90" height="90" viewBox="0 0 90 90"><circle cx="45" cy="45" r="42" fill="var(--red)" stroke="#fff" stroke-width="4"/><circle cx="45" cy="42" r="14" fill="none" stroke="#fff" stroke-width="3"/><path d="M45 34l3 6 6 1-4 4 1 6-6-3-6 3 1-6-4-4 6-1z" fill="#fff"/><path d="M37 55l-4 12 7-3 5 5M53 55l4 12-7-3-5 5" fill="none" stroke="#fff" stroke-width="2.5"/></svg>
  <svg class="abs" style="left:400px;top:511px" width="90" height="90" viewBox="0 0 90 90"><circle cx="45" cy="45" r="42" fill="var(--red)" stroke="#fff" stroke-width="4"/><rect x="28" y="30" width="34" height="28" rx="2" fill="none" stroke="#fff" stroke-width="3"/><path d="M34 40h22M34 47h22M34 54h14" stroke="#fff" stroke-width="2.5"/></svg>
  <svg class="abs" style="left:706px;top:511px" width="90" height="90" viewBox="0 0 90 90"><circle cx="45" cy="45" r="42" fill="var(--red)" stroke="#fff" stroke-width="4"/><rect x="31" y="42" width="28" height="22" rx="3" fill="#fff"/><path d="M36 42v-6a9 9 0 0 1 18 0v6" fill="none" stroke="#fff" stroke-width="3.5"/><circle cx="45" cy="52" r="3" fill="var(--red)"/></svg>

  <div class="why-title abs right-align" style="left:93px;width:260px;top:202px">Exclusive Access</div>
  <div class="why-text abs right-align" style="left:93px;top:236px">We work directly with celebrities and their management teams to deliver authentic, unforgettable experiences.</div>
  <div class="why-title abs" style="left:841px;top:202px">Custom Experiences</div>
  <div class="why-text abs" style="left:841px;top:236px">Every event is unique. We tailor each booking to fit your vision, budget, and audience.</div>
  <div class="why-title abs right-align" style="left:93px;width:260px;top:489px">Proven Track Record</div>
  <div class="why-text abs right-align" style="left:93px;top:523px">From Meridian 400 companies to private clients, we’ve orchestrated events with some of the most famous names in the world.</div>
  <div class="why-title abs" style="left:841px;top:489px">Confidential &amp; Professional</div>
  <div class="why-text abs" style="left:841px;top:523px">Our clients trust us to deliver world-class experiences with complete discretion and flawless execution.</div>
</section>

<!-- GET A QUOTE -->
<section class="quote abs">
  <div class="ghost abs" style="left:120px;top:20px;font-size:200px;color:#171a60">GET QUOTE</div>
  <h2 class="display abs">Let’s Make It Happen</h2>
  <p class="abs">Whether you’re planning a corporate retreat, a milestone celebration, or a private experience you’ll never forget, LumaHours.com is your partner in making it extraordinary.</p>
  <div class="btn-wrap" style="left:107px;top:353px;width:460px;height:55px"><span class="btn">If you can dream it, we can make it happen. <svg viewBox="0 0 9 12"><path d="M2 1l5 5-5 5" stroke="#fff" stroke-width="2" fill="none"/></svg></span></div>

  <div class="form-card abs">
    <svg class="abs" style="left:142px;top:-50px" width="74" height="74" viewBox="0 0 74 74"><circle cx="37" cy="37" r="34" fill="var(--red)" stroke="#fff" stroke-width="4"/><path d="M25 30h9v9l-5 8h-4l3-8h-3zM40 30h9v9l-5 8h-4l3-8h-3z" fill="#fff"/></svg>
    <h3 class="display">Get a Free Quote</h3>
    <div class="field" style="left:20px;top:108px;width:155px">First Name</div>
    <div class="field" style="left:185px;top:108px;width:155px">Last Name</div>
    <div class="field" style="left:20px;top:150px;width:155px">Email</div>
    <div class="field" style="left:185px;top:150px;width:155px">Phone</div>
    <div class="field" style="left:20px;top:192px;width:320px;height:98px">Message</div>
    <div class="btn-wrap" style="left:82px;top:303px;width:190px;height:48px"><span class="btn">Submit now <svg viewBox="0 0 9 12"><path d="M2 1l5 5-5 5" stroke="#fff" stroke-width="2" fill="none"/></svg></span></div>
  </div>
</section>

<!-- FOOTER -->
<footer class="footer abs">
  <div class="logo abs" style="left:107px;top:145px;font-size:42px">Gold Roster</div>
  <nav class="foot-links abs"><span>Our Talent</span><span>Past Client Experiences</span><span>About Us</span><span>Our Process</span><span>Ideas</span><span>Business Opportunities</span></nav>
  <div class="foot-contact abs">
    <span><svg viewBox="0 0 14 14"><rect x="1" y="3" width="12" height="8" rx="1" fill="#fff"/><path d="M1 3l6 5 6-5" stroke="var(--footer)" fill="none"/></svg>hello@goldroster.com</span>
    <span><svg viewBox="0 0 14 14"><path d="M3 1l3 3-1.5 2a8 8 0 0 0 3.5 3.5L10 8l3 3-2 2C6 13 1 8 1 3z" fill="#fff"/></svg>(555) 018-2947</span>
  </div>
  <div class="divider abs"></div>
  <div class="foot-social abs"><i></i><i></i><i></i><i></i><i></i></div>
  <div class="copy abs">Copyright © <b>GOLDROSTER</b> All Rights Reserved.</div>
</footer>
<svg class="abs" style="left:0;top:4470px" width="1200" height="130" viewBox="0 0 1200 130">
  <polygon points="0,130 599,11 1200,130 1200,100 599,0 0,100" fill="var(--red)"/>
  <polygon points="0,100 599,0 1200,100 1200,0 0,0" fill="var(--navy)"/>
</svg>

</body>
</html>
```